依頼詳細
プロが業務用の高圧洗浄機を使い、ご自宅の外構・駐車場(ガレージ)・ブロック塀・玄関タイル・を綺麗にされたい方を募集します。
泥、排気ガスの汚れ、コケ、ほこり等を綺麗に致します。
お見積りは無料
高圧洗浄専門店
割引制度有
平日割引あり(火曜日・水曜日は特別料金にて実施)(空き状況はお電話にてご確認下さい)
施工料金等、丁寧に分かりやすくご説明します。
作業時間平均:2時間~3時間
料金:33,000円~
作業時:水道をお借りします
まずは、お気軽にご相談下さい。
株式会社ミドリノハウジング
TEL:094ー318-5562
担当:坂巻(さかまき)・梅沢(うめざわ)
営業時間:9:00~19:00

記載項目
株式会社ミドリノハウジング
094-318-5562
料金:33,000円~(範囲によって異なります)
プロの高圧洗浄はミドリノハウジングにお任せください。
サイズ
A4
ページ数
片面
希望イメージ
シンプル 複雑
単色 カラフル
暗い 明るい
日常 高級
遊び心 厳粛
未来的 伝統的
女性的 男性的
希望する色
水色系、ターコイズブルーの使用をお願い致します。
納品ファイル
• 高解像度JPG (.jpg)
補足説明
会社ロゴを添付しておりますので、ロゴの使用をお願い致します。
■ 選んだ理由

見やすく、弊社希望のチラシに近いものでした。
頂きました案件全てのチラシ案を印刷し、三つ折りにしましたが、一番良かったです。
伝えたい内容も、しっかり入っており、戸建てとなると年配の方が多いと思われ、その点でも大事な部分は文字が大きく見やすさも良く選ばせて頂きました。

■ 提案者全員のお礼・コメント

初めての依頼となりましたが、多数の応募を頂きましてありがとうございました。
正直、こんなに多数の応募を頂けるとは思ってませんでしたので驚きました。
今後もチラシの案をご依頼する事もるかと思いますので、宜しくお願い致します。

```html
<!DOCTYPE html>
<html lang="ja">
<head>
<meta charset="UTF-8">
<title>外壁洗浄 高圧洗浄機 チラシ</title>
<link rel="stylesheet" href="https://fonts.googleapis.com/css2?family=Noto+Sans+JP:wght@400;500;700;900&display=swap">
<style>
  :root {
    --blue: #1a86c8;
    --blue-deep: #0d5f9e;
    --turquoise: #2bb3d6;
    --red: #d7262d;
    --ink: #2a2a2a;
    --white: #ffffff;
    --pale: #eef7fc;
  }
  * { box-sizing: border-box; margin: 0; padding: 0; }
  html, body { width: 848px; height: 1200px; overflow: hidden; background: var(--white); }
  body { font-family: "Noto Sans JP", sans-serif; color: var(--ink); }
  .flyer { position: relative; width: 848px; height: 1200px; overflow: hidden; }

  .hero-photo {
    position: absolute; left: 0; top: 0; width: 848px; height: 620px;
    background: linear-gradient(160deg, #9fb7c9 0%, #c9d6df 35%, #7f98a8 70%, #4f6a7c 100%);
  }
  .hero-title {
    position: absolute; left: 30px; top: 34px; padding: 6px 22px;
    background: var(--blue); color: var(--white);
    font-size: 58px; font-weight: 900; letter-spacing: 4px;
  }
  .badge-free {
    position: absolute; right: 36px; top: 36px; width: 210px; padding: 6px 0;
    background: var(--white); color: var(--blue-deep); text-align: center;
    font-size: 40px; font-weight: 900; border: 3px solid var(--blue);
  }
  .badge-plan {
    position: absolute; right: 36px; top: 104px; width: 210px; padding: 8px 0;
    background: var(--blue); color: var(--white); text-align: center;
    font-size: 24px; font-weight: 700; line-height: 1.3;
  }
  .headline { position: absolute; left: 30px; top: 150px; display: grid; grid-template-columns: 190px 190px; gap: 26px 40px; }
  .headline .char {
    width: 190px; height: 190px; display: flex; align-items: center; justify-content: center;
    background: var(--white); border: 6px solid var(--red);
    font-size: 150px; font-weight: 900; color: var(--blue-deep); line-height: 1;
  }
  .headline .char:nth-child(2), .headline .char:nth-child(3) { color: var(--red); border-color: var(--blue); }

  .lead { position: absolute; left: 0; top: 640px; width: 848px; text-align: center; font-size: 31px; font-weight: 700; line-height: 1.45; }
  .lead em { font-style: normal; color: var(--blue); }

  .areas { position: absolute; left: 34px; top: 748px; display: flex; gap: 20px; }
  .area { width: 180px; text-align: center; }
  .area-label { display: inline-block; background: var(--turquoise); color: var(--white); font-size: 22px; font-weight: 700; padding: 2px 20px; border-radius: 16px; margin-bottom: 6px; }
  .area-photo { width: 180px; height: 110px; border: 3px solid var(--turquoise); background: linear-gradient(160deg, #b8c3c8, #7c8a8f); }

  .pro-band {
    position: absolute; left: 0; top: 906px; width: 848px; height: 56px;
    background: var(--blue); color: var(--white); text-align: center;
    font-size: 32px; font-weight: 900; line-height: 56px; letter-spacing: 2px;
  }

  .price { position: absolute; left: 34px; top: 976px; width: 250px; }
  .price-label { display: inline-block; background: var(--blue-deep); color: var(--white); font-size: 22px; font-weight: 700; padding: 2px 12px; }
  .price-value { font-size: 46px; font-weight: 900; color: var(--red); line-height: 1.15; }
  .price-value small { font-size: 28px; }
  .price-note { font-size: 15px; }

  .terms { position: absolute; left: 300px; top: 978px; list-style: none; font-size: 22px; font-weight: 700; line-height: 1.55; }
  .terms li::before { content: "●"; color: var(--blue); margin-right: 4px; }
  .terms small { font-size: 17px; font-weight: 500; }

  .footer { position: absolute; left: 0; top: 1092px; width: 848px; height: 108px; border-top: 4px solid var(--blue); display: flex; align-items: center; padding: 0 30px; gap: 24px; }
  .company { display: flex; align-items: center; gap: 12px; }
  .company-mark { width: 48px; height: 48px; background: var(--turquoise); }
  .company-name { font-size: 20px; font-weight: 700; color: var(--blue-deep); line-height: 1.35; }
  .contact { flex: 1; text-align: center; }
  .contact-lead { font-size: 16px; font-weight: 700; color: var(--blue-deep); }
  .tel { display: flex; align-items: center; justify-content: center; gap: 6px; font-size: 40px; font-weight: 900; color: var(--red); line-height: 1.1; }
  .hours { font-size: 15px; }
  .staff { font-size: 16px; font-weight: 700; line-height: 1.4; border-left: 3px solid var(--blue); padding-left: 10px; }
</style>
</head>
<body>
<main class="flyer">
  <div class="hero-photo" role="img" aria-label="住宅の外壁に高圧洗浄機で水を噴射している作業風景"></div>
  <h1 class="hero-title">高圧洗浄機</h1>
  <div class="badge-free">見積無料</div>
  <div class="badge-plan">平日格安<br>プラン実施中</div>
  <div class="headline" aria-label="外壁洗浄">
    <span class="char">外</span><span class="char">壁</span>
    <span class="char">洗</span><span class="char">浄</span>
  </div>

  <p class="lead">泥や排気ガスの汚れ、コケ、ほこり等を<br>洗い流し<em>キレイに蘇らせる</em>高圧洗浄！</p>

  <section class="areas">
    <div class="area"><span class="area-label">外溝</span><div class="area-photo" role="img" aria-label="洗浄された外構の写真"></div></div>
    <div class="area"><span class="area-label">駐車場</span><div class="area-photo" role="img" aria-label="洗浄された駐車場の写真"></div></div>
    <div class="area"><span class="area-label">ブロック塀</span><div class="area-photo" role="img" aria-label="洗浄中のブロック塀の写真"></div></div>
    <div class="area"><span class="area-label">玄関</span><div class="area-photo" role="img" aria-label="洗浄された玄関タイルの写真"></div></div>
  </section>

  <div class="pro-band">プロによる高圧洗浄を承ります！</div>

  <section class="price">
    <span class="price-label">施工料金</span>
    <div class="price-value">33.000円<small>〜</small></div>
    <div class="price-note">範囲によって異なります</div>
  </section>

  <ul class="terms">
    <li>平日割引あり <small>(火曜日・水曜日は特別料金にて実施)</small></li>
    <li>空き状況はお電話にてご確認下さい</li>
    <li>作業時間：2〜3時間 <small>(水道をお借りします)</small></li>
  </ul>

  <footer class="footer">
    <div class="company">
      <span class="company-mark"></span>
      <div class="company-name">高圧洗浄専門店<br>(株) ミドリノハウジング</div>
    </div>
    <div class="contact">
      <div class="contact-lead">先ずはお気軽にお問合せください</div>
      <div class="tel">
        <svg width="34" height="34" viewBox="0 0 24 24" aria-hidden="true"><path fill="#d7262d" d="M6.6 10.8a15.1 15.1 0 0 0 6.6 6.6l2.2-2.2a1 1 0 0 1 1-.25 11.4 11.4 0 0 0 3.6.57 1 1 0 0 1 1 1V20a1 1 0 0 1-1 1A17 17 0 0 1 3 4a1 1 0 0 1 1-1h3.5a1 1 0 0 1 1 1c0 1.25.2 2.45.57 3.57a1 1 0 0 1-.25 1z"/></svg>
        094-318-5562
      </div>
      <div class="hours">営業時間：9:00〜19:00</div>
    </div>
    <div class="staff">担当<br>さかまき<br>うめざわ</div>
  </footer>
</main>
</body>
</html>
```